Restoration Specialist in need of business card designs

One side of the business card is a bathroom ripped out down to the studs with just a sink and toilet and then the other side is the bathroom (same sink and toilet) but put back together. Like a before and after on each side behind our information. Stand out, hard to forget, business cards for my restoration company. I want a unique concept all together.
Must include in no particular order:
our business name "Summit Renewals"
Possible Logo for a restoration company
Owner; Dennis Moravec
410-386-7294
dmoravec@summitrenewalsqx.example
SummitRenewalsQX.example (our company website) BUT I am open to any and all designs and options.

Target Market(s)

Customers, Men in the mitigation, plumbing, electrical, HVAC, Roofing, insurance companies

Industry/Entity Type

Restoration/ construction

Contact Information for Business Card

Must include in no particular order: our business name "Summit Renewals" Owner; Dennis Moravec 410-386-7294 dmoravec@summitrenewalsqx.example SummitRenewalsQX.example (our company website) MAY include a list of our services: Residential~ Emergency Response ~ Board- up~ Complete Restoration

Font styles to use
Serif

Colors
0054AA
0677BA
7BADD7
CADEEF
E8F1F8
F0912C
F2A743
F7CA91
FBE8D2
FDF5EE

Requirements
Must have
• unique, memorable, not something men have seen over and over again,
Nice to have
• eye catching
Should not have
• Been something I could have made by myself

```html
<!DOCTYPE html>
<html lang="en">
<head>
<meta charset="utf-8">
<title>Summit Renewals – Business Card</title>
<link rel="stylesheet" href="https://fonts.googleapis.com/css2?family=Noto+Serif:ital,wght@0,400;0,700;1,400&display=swap">
<style>
  :root {
    --navy: #12334d;
    --orange: #f07a1f;
    --white: #ffffff;
    --ink: #1d2a36;
    --stage: #d9dde1;
    --silver-light: #f4f4f4;
    --silver-dark: #222428;
  }
  * { box-sizing: border-box; margin: 0; padding: 0; }
  html, body {
    width: 1200px; height: 1122px; overflow: hidden;
    background: var(--stage);
    font-family: "Noto Serif", Georgia, serif;
  }
  .canvas { position: relative; width: 1200px; height: 1122px; }
  .card {
    position: absolute; left: 220px; width: 760px; height: 434px;
    border-radius: 24px; overflow: hidden;
    box-shadow: 0 14px 30px rgba(0,0,0,.25);
  }
  .card-front { top: 96px; background: var(--white); }
  .card-back { top: 592px; background: var(--navy); }
  .card-art { position: absolute; inset: 0; width: 100%; height: 100%; }

  .accent-bar {
    position: absolute; left: 64px; top: 40px; width: 14px; height: 118px;
    background: var(--navy);
  }
  .identity { position: absolute; left: 122px; top: 44px; }
  .person-name {
    font-weight: 700; font-size: 38px; letter-spacing: 2px;
    color: var(--navy); text-transform: uppercase; line-height: 1;
  }
  .person-role {
    font-style: italic; font-size: 19px; color: var(--orange); margin-top: 2px;
  }
  .contact-list { list-style: none; margin-top: 14px; }
  .contact-list li {
    display: flex; align-items: center; gap: 10px;
    font-size: 16px; color: var(--ink); line-height: 1.6;
  }
  .contact-list svg { width: 15px; height: 15px; flex: none; }

  .services { position: absolute; left: 96px; top: 236px; }
  .services-title {
    font-weight: 700; font-size: 18px; letter-spacing: 1.5px;
    color: var(--navy); text-transform: uppercase;
  }
  .service-list { list-style: none; margin-top: 4px; }
  .service-list li {
    display: flex; align-items: center; gap: 9px;
    font-size: 14.5px; letter-spacing: 1px; color: var(--ink);
    text-transform: uppercase; line-height: 1.55;
  }
  .bullet {
    width: 10px; height: 10px; flex: none;
    display: grid; grid-template-columns: 1fr 1fr; gap: 1px;
  }
  .bullet i:nth-child(1), .bullet i:nth-child(4) { background: var(--orange); }
  .bullet i:nth-child(2), .bullet i:nth-child(3) { background: var(--navy); }

  .brand {
    position: absolute; left: 360px; top: 190px;
    display: flex; align-items: center; gap: 16px;
  }
  .brand-square { width: 26px; height: 26px; background: var(--orange); }
  .brand-name {
    font-weight: 700; font-size: 44px; color: var(--orange); line-height: 1.05;
  }
</style>
</head>
<body>
<main class="canvas">

  <section class="card card-front" aria-label="Card front with contact details">
    <svg class="card-art" viewBox="0 0 760 434" aria-hidden="true">
      <polygon points="300,434 760,290 760,326 380,434" fill="var(--navy)"/>
      <rect x="640" y="292" width="66" height="50" fill="var(--navy)"/>
      <rect x="616" y="362" width="70" height="56" fill="var(--orange)"/>
    </svg>
    <div class="accent-bar"></div>
    <div class="identity">
      <h1 class="person-name">Dennis Moravec</h1>
      <p class="person-role">Owner</p>
      <ul class="contact-list">
        <li>
          <svg viewBox="0 0 24 24"><path fill="var(--orange)" d="M6.6 10.8a15.1 15.1 0 0 0 6.6 6.6l2.2-2.2a1 1 0 0 1 1-.25 11.4 11.4 0 0 0 3.6.57 1 1 0 0 1 1 1V20a1 1 0 0 1-1 1A17 17 0 0 1 3 4a1 1 0 0 1 1-1h3.5a1 1 0 0 1 1 1c0 1.25.2 2.45.57 3.57a1 1 0 0 1-.25 1z"/></svg>
          410-386-7294
        </li>
        <li>
          <svg viewBox="0 0 24 24"><rect x="2" y="5" width="20" height="14" fill="var(--orange)"/><path d="M2 5l10 8 10-8" fill="none" stroke="#fff" stroke-width="1.6"/></svg>
          dmoravec@summitrenewalsqx.example
        </li>
        <li>
          <svg viewBox="0 0 24 24"><circle cx="12" cy="12" r="10" fill="var(--orange)"/><path d="M2 12h20M12 2c3 3 3 17 0 20M12 2c-3 3-3 17 0 20" fill="none" stroke="#fff" stroke-width="1.4"/></svg>
          SummitRenewalsQX.example
        </li>
      </ul>
    </div>
    <div class="services">
      <h2 class="services-title">Our Service</h2>
      <ul class="service-list">
        <li><span class="bullet"><i></i><i></i><i></i><i></i></span>Residential</li>
        <li><span class="bullet"><i></i><i></i><i></i><i></i></span>Emergency Response</li>
        <li><span class="bullet"><i></i><i></i><i></i><i></i></span>Board-Up</li>
        <li><span class="bullet"><i></i><i></i><i></i><i></i></span>Storm Protection</li>
        <li><span class="bullet"><i></i><i></i><i></i><i></i></span>Complete Restoration</li>
      </ul>
    </div>
  </section>

  <section class="card card-back" aria-label="Card back with company name">
    <svg class="card-art" viewBox="0 0 760 434" aria-hidden="true">
      <defs>
        <linearGradient id="silver-band" x1="0" y1="0" x2="1" y2="0">
          <stop offset="0" stop-color="var(--silver-light)"/>
          <stop offset="0.35" stop-color="#8d9095"/>
          <stop offset="1" stop-color="var(--silver-dark)"/>
        </linearGradient>
        <linearGradient id="silver-square" x1="0" y1="0" x2="1" y2="1">
          <stop offset="0" stop-color="#ffffff"/>
          <stop offset="1" stop-color="#9ea2a7"/>
        </linearGradient>
      </defs>
      <polygon points="150,0 196,0 340,434 292,434" fill="url(#silver-band)"/>
      <rect x="36" y="140" width="74" height="56" fill="var(--orange)"/>
      <rect x="26" y="214" width="74" height="56" fill="url(#silver-square)"/>
    </svg>
    <div class="brand">
      <span class="brand-square"></span>
      <p class="brand-name">Summit Renewals</p>
    </div>
  </section>

</main>
</body>
</html>
```